Brackwater Vale Medical Website to make connecting and communicating easier

To create a unique, user-friendly, professional website for patients and professionals to access education/ information, forms, appointments, contact details, and data about us, and for us to have the capacity to link to various cloud-based platforms.
To use the logo design and colour scheme we have just sourced.

WEBSITE to be eye catching, Inspiring and alluring
- efficient and logical
- professional and trustworthy appearance
- health focus "living health matters"
- user friendly
- ability to link with cloud-based software and video conferencing tools/ telehealth
- colours- black/ white teal and ?silver

PAGES:
page 1 - Our clinic and staff, services offered, contact us- address/ map / contact details- social media connections
page 2- patients and visitors - New patient forms to complete, news and patient informtion (educatinal)
page 3 - health professionals -referral forms, research and education
page 3- online appointments
page 4 - Quick links - partners, other services
page 5- privacy policy, disclaimer

Need extra days to review

HI, Could we please extend the deadline another 5 days, so sorry just struggling with my workload to be able to keep up and I am wanting to liaise more with the designer that I will choose. I am so happy with PixelForge and all the designers - thank you! Thank you so much!!

Target Market(s)

Patients - mostly over 60's so the website must be minimal clicks and simple to navigate
Professionals - for education and access forms

Industry/Entity Type

Health Care

Coding

Coded - Design and coding required

Number of Pages Required

5+ page

Font styles to use
Sans Serif
Script

Colors
33b8a4
86cfc6

Requirements
Must have
• WEBSITE to be eye catching, Inspiring and alluring
- efficient and logical
- user friendly

WEBSITE - professional and user friendly
- ability to link with cloud based software and videoconferencing/ telehealth
Nice to have
• clean and crisp presentation
happy for an innovative look
room to add more services and ability to link pages and resources
Should not have
• Please ensure the website is not:
clunky
difficult to navigate
common and cheap looking

```html
<!DOCTYPE html>
<html lang="en">
<head>
<meta charset="utf-8">
<title>Appointments – Brackwater Vale Medical</title>
<link href="https://fonts.googleapis.com/css2?family=Roboto:wght@400;500&display=swap" rel="stylesheet">
<style>
:root{
  --teal:#33b8a4;
  --mint:#bdf2ec;
  --ink:#222222;
  --body:#4a4a4a;
  --line:#33b8a4;
  --white:#ffffff;
}
*{box-sizing:border-box;margin:0;padding:0}
html,body{width:926px;height:1200px;overflow:hidden;background:var(--white)}
body{font-family:'Roboto',sans-serif;color:var(--ink);position:relative}
.abs{position:absolute}

/* header */
.site-header{position:absolute;left:0;top:0;width:926px;height:60px;background:var(--white)}
.brand{left:80px;top:20px;display:flex;align-items:center;gap:6px;font-size:11px;font-weight:500;color:var(--teal)}
.brand-dot{width:14px;height:14px;border-radius:50%;background:var(--teal)}
.main-nav a{position:absolute;top:26px;font-size:9.5px;color:var(--ink);text-decoration:none}
.main-nav a.active{color:var(--teal)}
.contact-btn{left:786px;top:17px;width:81px;height:29px;background:var(--teal);color:var(--white);font-size:8.5px;display:flex;align-items:center;justify-content:center;border-radius:2px}

/* hero */
.hero{left:0;top:60px;width:926px;height:289px;background:linear-gradient(110deg,#6f7478 0%,#9a9fa2 40%,#7d8386 70%,#585e63 100%)}
.hero-title{left:0;top:178px;width:926px;text-align:center;color:var(--white);font-size:22px}
.breadcrumb{left:0;top:217px;width:926px;text-align:center;color:var(--white);font-size:9px}
.breadcrumb span{margin:0 7px}

/* appointment */
.eyebrow{left:71px;top:422px;font-size:8.5px;color:var(--ink)}
.headline{left:71px;top:440px;width:360px;font-size:23px;font-weight:500;line-height:28px;color:var(--ink)}
.copy{left:71px;width:350px;font-size:9px;line-height:15.5px;color:var(--body)}
.field{width:163px;height:32px;border:1px solid var(--line);font-size:9.5px;color:var(--body);display:flex;align-items:center;padding-left:10px;gap:6px;background:var(--white)}
.caret{width:0;height:0;border-left:3px solid transparent;border-right:3px solid transparent;border-top:4px solid var(--ink)}
.confirm-btn{left:71px;top:784px;width:344px;height:31px;background:var(--teal);color:var(--white);font-size:9px;font-weight:500;display:flex;align-items:center;justify-content:center;border-radius:2px}
.photo-main{left:508px;top:413px;width:347px;height:408px;border-radius:26px;background:linear-gradient(150deg,#d9dcd8 0%,#e9e8e3 45%,#c9a889 70%,#dfe1dc 100%)}
.photo-inset{width:127px;height:152px;border:3px solid var(--white);border-radius:16px}
.photo-doctor{left:774px;top:440px;background:linear-gradient(160deg,#b7b0a3,#e8eaec 55%,#c9ccd0)}
.photo-visit{left:463px;top:631px;background:linear-gradient(200deg,#8d8f92,#e1e4e6 50%,#a47f66)}

/* footer */
.site-footer{left:0;top:886px;width:926px;height:267px;background:var(--mint)}
.foot-title{top:953px;font-size:15.5px;color:var(--ink)}
.foot-list{top:975px;list-style:none;font-size:9.5px;color:var(--body)}
.foot-list li{height:18.7px;line-height:18.7px}
.foot-text{left:75px;top:977px;width:160px;font-size:9.5px;line-height:15.5px;color:var(--body)}
.contact-line{left:75px;font-size:9px;color:var(--body);display:flex;align-items:center;gap:8px}
.social{top:1042px;width:12px;height:12px;border-radius:50%;background:var(--ink)}
.bottom-bar{left:0;top:1153px;width:926px;height:47px;background:var(--teal);color:var(--white);font-size:9.5px}
</style>
</head>
<body>

<header class="site-header">
  <div class="abs brand"><span class="brand-dot"></span>Brackwater Vale Medical</div>
  <nav class="main-nav">
    <a style="left:296px">Home</a>
    <a style="left:350px">Services</a>
    <a style="left:415px">Our Doctors</a>
    <a class="active" style="left:496px">Appoinments</a>
    <a style="left:579px">Patients &amp; visitors</a>
  </nav>
  <div class="abs contact-btn">Contacts Us</div>
</header>

<section class="abs hero" role="img" aria-label="Dentist treating a patient in a clinic chair"></section>
<h1 class="abs hero-title" style="font-weight:400">Appoinments</h1>
<div class="abs breadcrumb"><span>Home</span><span>Appoinments</span></div>

<main>
  <p class="abs eyebrow">Appointment</p>
  <h2 class="abs headline">Book an appointment with your doctor right away</h2>
  <p class="abs copy" style="top:507px">Sed ut perspiciatis unde omnis iste natus error sit voluptatem accusantium doloremque laudantium, totam rem aperiam, eaque ipsa quae ab illo inventore veritatis et quasi architecto beatae vitae dicta sunt explicabo.</p>
  <p class="abs copy" style="top:563px">Lorem ipsum dolor sit amet, consectetur adipiscing elit, sed do eiusmod tempor incididunt ut labore et dolore magna aliqua. Ut enim ad minim veniam, quis nostrud exercitation ullamco laboris nisi ut aliquip ex ea commodo consequat.</p>

  <div class="abs field" style="left:71px;top:639px">First name</div>
  <div class="abs field" style="left:253px;top:639px">Last name</div>
  <div class="abs field" style="left:71px;top:687px">Select doctor <span class="caret"></span></div>
  <div class="abs field" style="left:253px;top:687px;font-size:9px">Select departments <span class="caret"></span></div>
  <div class="abs field" style="left:71px;top:736px">Date and time</div>
  <div class="abs field" style="left:253px;top:736px">Contact number</div>
  <div class="abs confirm-btn">Confirm An Appointment</div>

  <div class="abs photo-main" role="img" aria-label="Doctor's hand writing on a clipboard"></div>
  <div class="abs photo-inset photo-doctor" role="img" aria-label="Senior doctor seated at a desk with a clipboard"></div>
  <div class="abs photo-inset photo-visit" role="img" aria-label="Doctor listening to a young patient with a stethoscope"></div>
</main>

<footer>
  <div class="abs site-footer"></div>

  <h3 class="abs foot-title" style="left:75px;font-weight:400">Contact Us</h3>
  <p class="abs foot-text">Lorem ipsum dolor sit amet, consectetur adipiscing elit, sed do eiusmod tempor incididunt</p>
  <div class="abs contact-line" style="top:1028px">
    <svg width="9" height="10" viewBox="0 0 9 10"><path d="M4.5 0a3.5 3.5 0 0 0-3.5 3.5C1 6 4.5 10 4.5 10S8 6 8 3.5A3.5 3.5 0 0 0 4.5 0zm0 5a1.4 1.4 0 1 1 0-2.8 1.4 1.4 0 0 1 0 2.8z" fill="#222"/></svg>
    14 Harbour Lane CA, USA</div>
  <div class="abs contact-line" style="top:1045px">
    <svg width="9" height="9" viewBox="0 0 9 9"><path d="M2 0.5l1.5 2-1 1c.6 1.3 1.7 2.4 3 3l1-1 2 1.5-1 1.5C4 8.5 0.5 5 0.5 1.5z" fill="#222"/></svg>
    +1-555-010-2040</div>
  <div class="abs contact-line" style="top:1062px">
    <svg width="9" height="7" viewBox="0 0 9 7"><rect x="0.5" y="0.5" width="8" height="6" fill="none" stroke="#222"/><path d="M0.5 0.5l4 3.2 4-3.2" fill="none" stroke="#222"/></svg>
    hello@brackwatervale.example</div>

  <h3 class="abs foot-title" style="left:308px;font-weight:400">Quick Links</h3>
  <ul class="abs foot-list" style="left:308px">
    <li>General information</li><li>Emergency service</li><li>Ambulance</li>
    <li>Medical research</li><li>Blood bank</li><li>Intensive care service</li>
  </ul>

  <h3 class="abs foot-title" style="left:471px;font-weight:400">Join Our Community</h3>
  <ul class="abs foot-list" style="left:471px">
    <li>Blog postes</li><li>Join our forum</li><li>Meet our doctors</li>
    <li>Medical research</li><li>Help center</li><li>Contract us</li>
  </ul>

  <h3 class="abs foot-title" style="left:705px;font-weight:400">Open Time</h3>
  <ul class="abs foot-list" style="left:705px;font-size:9px">
    <li>Mon-Fri 8:00 AM - 10:00 PM</li><li>Sat-Sun 9:00 AM - 6:00 PM</li><li>Emergency 24/24 hours</li>
  </ul>
  <span class="abs social" style="left:705px" aria-label="Social link"></span>
  <span class="abs social" style="left:735px" aria-label="Social link"></span>
  <span class="abs social" style="left:766px" aria-label="Social link"></span>
  <span class="abs social" style="left:796px" aria-label="Social link"></span>

  <div class="abs bottom-bar">
    <span class="abs" style="left:362px;top:17px">Copyright 2020 . All rights reserved</span>
    <span class="abs" style="left:543px;top:17px">Brackwater Vale</span>
  </div>
</footer>

</body>
</html>
```